Bluewater Ridge Commercial Svcs

I need a business card for my company in Orlando Florida. I provide all property maintenance/repair services both commercial and residential. We also do kitchen and bath remodels, full gut rehab and renovation, and painting. I do not have any suggestions for card layout. I want something that looks great that i can hand out to contractors and home owners to help generate business.

Target Market(s)

contractors, property owners, real estate property managers

Industry/Entity Type

Business

Contact Information for Business Card

Bluewater Ridge Commercial Services, Dale Morrow, 2186 Tamsey Ln. Orlando,FL 32811, Owner

```html
<!DOCTYPE html>
<html lang="en">
<head>
<meta charset="utf-8">
<title>Bluewater Ridge Commercial Services – Business Card</title>
<link href="https://fonts.googleapis.com/css2?family=Lato:wght@400;700;900&family=Questrial&display=swap" rel="stylesheet">
<style>
  :root {
    --backdrop: #2b2b2b;
    --card-white: #f7f7f7;
    --navy: #0d1a6b;
    --band-navy: #0c1870;
    --ink: #1c1c1c;
    --band-text: #d4d6de;
    --gold: #c99a2a;
    --gold-soft: #efe1b8;
  }
  * { margin: 0; padding: 0; box-sizing: border-box; }
  html, body {
    width: 1200px; height: 900px; overflow: hidden;
    background: var(--backdrop);
  }
  .business-card {
    position: absolute; left: 100px; top: 164px;
    width: 1000px; height: 572px;
    background: var(--card-white);
    overflow: hidden;
    box-shadow: 0 10px 30px rgba(0,0,0,.5);
    font-family: "Lato", sans-serif;
  }
  .service-band {
    position: absolute; left: 0; right: 0; top: 322px; bottom: 0;
    background: var(--band-navy);
  }
  .region-map {
    position: absolute; left: 720px; top: 42px;
    width: 230px; height: 150px;
    background: var(--gold-soft);
    border: 3px solid var(--gold);
    border-radius: 6px;
  }
  .owner-block { position: absolute; left: 62px; top: 190px; }
  .owner-name {
    font-weight: 900; font-size: 34px; color: var(--navy);
    letter-spacing: .5px; line-height: 1;
  }
  .owner-title {
    font-weight: 400; font-size: 26px; color: var(--ink);
    letter-spacing: 1px; margin-top: 4px;
  }
  .company-name {
    position: absolute; right: 44px; top: 268px;
    font-weight: 900; font-size: 40px; color: var(--navy);
    letter-spacing: .5px; white-space: nowrap;
  }
  .band-content {
    position: absolute; right: 44px; top: 348px;
    text-align: right; color: var(--band-text);
  }
  .service-line {
    font-weight: 700; font-size: 22px; line-height: 28px;
    letter-spacing: .4px; text-transform: uppercase;
  }
  .service-group + .service-group { margin-top: 10px; }
  .contact-list {
    margin-top: 14px; text-align: left; display: inline-block;
    font-family: "Questrial", sans-serif;
  }
  .contact-row {
    display: flex; align-items: center; gap: 16px;
    font-size: 25px; letter-spacing: 1px; line-height: 40px;
  }
  .contact-icon { width: 24px; height: 20px; fill: var(--band-text); flex: none; }
</style>
</head>
<body>
  <div class="business-card">
    <div class="service-band"></div>
    <div class="region-map" role="img" aria-label="Outline map of Florida with a star marking Orlando"></div>

    <div class="owner-block">
      <div class="owner-name">DALE MORROW</div>
      <div class="owner-title">OWNER</div>
    </div>

    <div class="company-name">BLUEWATER RIDGE COMMERCIAL SERVICES</div>

    <div class="band-content">
      <div class="service-group">
        <div class="service-line">Property Maintenance &amp;</div>
        <div class="service-line">Repair Services Commercial/Residential</div>
      </div>
      <div class="service-group">
        <div class="service-line">Kitchen &amp; Bath Remodels,</div>
        <div class="service-line">Renovations, Alterations &amp; Painting</div>
      </div>
      <div class="contact-list">
        <div class="contact-row">
          <svg class="contact-icon" viewBox="0 0 24 18" aria-hidden="true">
            <path d="M0 0h24v18H0z M2 2v1l10 7 10-7V2z M2 5v11h20V5l-10 7z" fill-rule="evenodd"/>
          </svg>
          <span>dmorrow1@bluewaterridge.com</span>
        </div>
        <div class="contact-row">
          <svg class="contact-icon" viewBox="0 0 24 20" aria-hidden="true">
            <path d="M12 0L0 10h3v10h7v-6h4v6h7V10h3z"/>
          </svg>
          <span>2186 Tamsey Ln. Orlando,FL 32811</span>
        </div>
      </div>
    </div>
  </div>
</body>
</html>
```